Real Estate Listing Signs for standard Yard arms

I need real estate listing signs done, for the standard sized sign to be hung beneath a white yard arm. To match existing logo. Information to be included:
-Logo
-Business name
-Phone number
-Marden Fosk Tundra Circle & Marden Fosk realty logos (smaller print)

Colors to be Red and anywhere in the gray scale between black and white, or a combination of those.

Target Market(s)

Drive by visuals

Industry/Entity Type

Real Estate Agent

Colors

Designer to choose only greyscale colors for use in the design.

Requirements
Must have
• My Logo and business name in same/similar font to whats provided, the MF tundra circle logo (small on bottom or corner somewhere), My phone number, and a decent amount of red coloration on the sign.

```html
<!DOCTYPE html>
<html lang="en">
<head>
<meta charset="utf-8">
<title>Virkstrom Realty Yard Sign</title>
<link rel="stylesheet" href="https://fonts.googleapis.com/css2?family=Montserrat:wght@400;500;700&family=Noto+Sans:wght@700&display=swap">
<style>
  :root {
    --sign-grey: #e6e7e9;
    --brand-red: #fe1020;
    --ink-black: #000000;
    --ink-white: #ffffff;
    --ink-charcoal: #4d4e52;
  }
  * { margin: 0; padding: 0; box-sizing: border-box; }
  html, body {
    width: 1200px;
    height: 457px;
    overflow: hidden;
    background: var(--sign-grey);
  }
  .sign {
    position: relative;
    width: 1200px;
    height: 457px;
    background: var(--sign-grey);
  }
  .brand-mark {
    position: absolute;
    left: 160px;
    top: 104px;
    width: 138px;
    height: 138px;
    background: var(--brand-red);
  }
  .business-name {
    position: absolute;
    left: 60px;
    width: 336px;
    top: 322px;
    text-align: center;
    font-family: "Noto Sans", sans-serif;
    font-weight: 700;
    font-size: 31px;
    letter-spacing: 0.5px;
    color: var(--ink-black);
    white-space: nowrap;
  }
  .agent-band {
    position: absolute;
    left: 457px;
    top: 102px;
    width: 743px;
    height: 253px;
    background: var(--brand-red);
    color: var(--ink-white);
    font-family: "Montserrat", sans-serif;
    padding: 42px 0 0 78px;
  }
  .agent-name {
    font-weight: 700;
    font-size: 48px;
    line-height: 58px;
    letter-spacing: 0.5px;
    white-space: nowrap;
  }
  .agent-phone,
  .agent-email {
    font-weight: 500;
    font-size: 46px;
    line-height: 57px;
    white-space: nowrap;
  }
  .brokerage-name {
    position: absolute;
    left: 457px;
    top: 390px;
    font-family: "Montserrat", sans-serif;
    font-weight: 700;
    font-size: 24px;
    color: var(--ink-charcoal);
    white-space: nowrap;
  }
  .office-disclaimer {
    position: absolute;
    left: 835px;
    top: 399px;
    font-family: "Montserrat", sans-serif;
    font-weight: 500;
    font-size: 14.5px;
    line-height: 19px;
    color: var(--ink-black);
    white-space: nowrap;
  }
</style>
</head>
<body>
  <main class="sign">
    <div class="brand-mark" aria-hidden="true"></div>
    <p class="business-name">VIRKSTROM REALTY</p>

    <section class="agent-band">
      <h1 class="agent-name">DANA VIRKSTROM</h1>
      <p class="agent-phone">907-555-0148</p>
      <p class="agent-email">dvirkstrom@mailbox.com</p>
    </section>

    <p class="brokerage-name">MF TUNDRA CIRCLE</p>

    <p class="office-disclaimer">EACH OFFICE INDEPENDENTLY<br>OWNED AND OPERATED</p>
  </main>
</body>
</html>
```